Wren's Hearth Support Business Card

Business card design
Font must be in Poppins Regular for Wren's Hearth Support
Safe Days Ahead font is Alex Brush

Colour must be Hex #910E2B
RGB 145-14-43
Pantone 7427 C
We want the card editable
On the front please include
Name eg Mavis Dunleavy
Position eg Clinical Care Manager
Phone number mobile 0473 856 342
Phone 08 7394 2650
Email : mavis@wrenshearthsupport.com.au
Address : Gullwing Cove, Western Australia, 6259
Website : wrenshearthsupport.com.au
Contact us today to experience the warmth, respect and personal touch of Wren's Hearth Support.

Target Market(s)

35+

Industry/Entity Type

aged care / community

Contact Information for Business Card

see project description

Requirements
Must have
• Colours, logos and fonts as detailed and uploaded

```html
<!DOCTYPE html>
<html lang="en">
<head>
<meta charset="utf-8">
<title>Wren's Hearth Support – Business Card</title>
<link href="https://fonts.googleapis.com/css2?family=Alex+Brush&family=Poppins:wght@400;700&display=swap" rel="stylesheet">
<style>
  :root{
    --brand:#910E2B;
    --brand-soft:#b86677;
    --band-mid:#c98798;
    --band-light:#dcb2bc;
    --blush:#d3a2ae;
    --paper:#ffffff;
    --stage:#cbcbcb;
    --ink:#111111;
    --bloom-a:#e85a48;
    --bloom-b:#f08a70;
  }
  *{margin:0;padding:0;box-sizing:border-box}
  html,body{width:1200px;height:1111px;overflow:hidden;background:var(--stage)}
  body{font-family:"Poppins",sans-serif}
  .stage{position:absolute;left:0;top:0;width:1600px;height:1481px;transform:scale(.75);transform-origin:0 0}
  .side-label{position:absolute;font-weight:700;font-size:40px;line-height:1;color:var(--brand);letter-spacing:.5px}
  .side-label--front{left:98px;top:57px}
  .side-label--back{left:494px;top:748px}
  .card{position:absolute;width:1004px;height:590px;background:var(--paper);overflow:hidden}
  .card--front{left:100px;top:100px}
  .card--back{left:496px;top:790px}
  .card__art{position:absolute;inset:0;width:100%;height:100%}
  .flower-spray{position:absolute;border-radius:50% 50% 20px 20px;
    background:radial-gradient(circle at 45% 30%,var(--bloom-b),var(--bloom-a) 55%,rgba(232,90,72,.2) 100%)}
  .card--front .flower-spray{left:62px;top:212px;width:136px;height:180px}
  .card--back .flower-spray{left:845px;top:420px;width:138px;height:170px}

  .brand{position:absolute;left:308px;top:230px;display:flex;align-items:flex-start}
  .brand__dot{width:124px;height:124px;border-radius:50%;border:6px solid var(--brand);flex:none;margin-top:2px}
  .brand__text{margin-left:14px;color:var(--brand)}
  .brand__name{font-weight:400;font-size:44px;line-height:48px;color:var(--brand)}
  .brand__tagline{font-family:"Alex Brush",cursive;font-size:36px;line-height:36px;margin-top:2px;color:var(--brand)}

  .person{position:absolute;left:60px;top:44px}
  .person__name{font-weight:700;font-size:37px;line-height:42px;color:var(--brand);letter-spacing:-.3px;text-transform:uppercase}
  .person__role{font-size:26px;line-height:32px;color:var(--ink)}

  .contacts{position:absolute;left:58px;top:250px;list-style:none}
  .contacts li{display:flex;align-items:center;height:62px;color:var(--paper);font-size:28.5px;white-space:nowrap}
  .contacts svg{width:28px;height:28px;margin-right:16px;flex:none;fill:none;stroke:var(--paper);stroke-width:2;stroke-linecap:round;stroke-linejoin:round}
</style>
</head>
<body>
<div class="stage">
  <div class="side-label side-label--front">FRONT</div>
  <section class="card card--front">
    <svg class="card__art" viewBox="0 0 1004 590" aria-hidden="true">
      <defs>
        <linearGradient id="waveFront" x1="0" y1="0" x2="1" y2="1">
          <stop offset="0" stop-color="#9e2f48"/><stop offset="1" stop-color="#b86677"/>
        </linearGradient>
        <linearGradient id="bandFront" x1="0" y1="0" x2="1" y2="1">
          <stop offset="0" stop-color="#c07e8f"/><stop offset="1" stop-color="#e0bcc5"/>
        </linearGradient>
      </defs>
      <path d="M535 0 C640 110 760 275 1004 275 L1004 0 Z" fill="url(#bandFront)"/>
      <path d="M560 0 C650 80 760 200 1004 168 L1004 0 Z" fill="url(#waveFront)"/>
      <path d="M0 322 C130 300 210 430 383 590 L0 590 Z" fill="var(--blush)"/>
      <path d="M0 332 C120 360 205 435 338 590 L0 590 Z" fill="url(#waveFront)"/>
    </svg>
    <div class="flower-spray" role="img" aria-label="Watercolour spray of red poppy flowers"></div>
    <div class="brand">
      <div class="brand__dot"></div>
      <div class="brand__text">
        <div class="brand__name">Wren's<br>Hearth Support</div>
        <div class="brand__tagline">Safe Days Ahead</div>
      </div>
    </div>
  </section>

  <div class="side-label side-label--back">BACK</div>
  <section class="card card--back">
    <svg class="card__art" viewBox="0 0 1004 590" aria-hidden="true">
      <defs>
        <linearGradient id="waveBack" x1="0" y1="0" x2="1" y2="1">
          <stop offset="0" stop-color="#c98798"/><stop offset="1" stop-color="#a8485f"/>
        </linearGradient>
      </defs>
      <path d="M578 0 C660 70 790 135 1004 100 L1004 0 Z" fill="url(#waveBack)"/>
      <path d="M0 590 L0 400 C200 300 420 280 510 292 C700 300 850 420 970 590 Z" fill="var(--band-light)"/>
      <path d="M0 590 L0 200 C150 160 250 165 310 172 C440 190 530 250 610 330 L870 590 Z" fill="var(--band-mid)"/>
      <path d="M0 195 C110 165 200 155 260 157 C380 162 470 220 540 300 L805 590 L0 590 Z" fill="var(--brand)"/>
    </svg>
    <div class="flower-spray" role="img" aria-label="Watercolour spray of red poppy flowers"></div>

    <div class="person">
      <div class="person__name">Mavis Dunleavy</div>
      <div class="person__role">Clinical Care Manager</div>
    </div>

    <ul class="contacts">
      <li><svg viewBox="0 0 24 24"><rect x="7" y="3" width="10" height="18" rx="2"/><path d="M11 18h2"/></svg>0473 856 342</li>
      <li><svg viewBox="0 0 24 24"><path d="M5 4l3 0 2 5-2 1.5a11 11 0 0 0 5.5 5.5L15 14l5 2v3a2 2 0 0 1-2 2A16 16 0 0 1 3 6a2 2 0 0 1 2-2z"/><path d="M14 3a7 7 0 0 1 7 7M14 7a3 3 0 0 1 3 3"/></svg>08 7394 2650</li>
      <li><svg viewBox="0 0 24 24"><circle cx="12" cy="12" r="9"/><path d="M3 12h18M12 3c3 3 3 15 0 18M12 3c-3 3-3 15 0 18"/></svg>mavis@wrenshearthsupport.com.au</li>
      <li><svg viewBox="0 0 24 24"><rect x="3" y="4" width="18" height="12" rx="1"/><path d="M9 20h6M12 16v4"/></svg>www.wrenshearthsupport.com.au</li>
      <li><svg viewBox="0 0 24 24"><path d="M12 18s-6-5.5-6-10a6 6 0 0 1 12 0c0 4.5-6 10-6 10z"/><circle cx="12" cy="8" r="2"/><path d="M6 22h12"/></svg>Gullwing Cove, Western Australia, 6259</li>
    </ul>
  </section>
</div>
</body>
</html>
```